Corvanta Energy LNG as Marine Fuel Powerpoint Design

Powerpoint template inspired by and using the attached Corvanta Energy logo. We are developing LNG as marine fuel facilities and bunkering vessels to supply the fuel to the marine industry. Designs should use the Corvanta Energy logo colors and be consistent with our vision of providing environmentally cleaner fuel supply. Our selected logo was 1A in the attached files, as shown on the business card template also attached.

Target Market(s)

Marine Industry (Shipping, container vessels, crude carriers, cargo / transportation vessels, etc.)

Requirements
Must have
• Clean / green energy theme
Compatibility with submitted logo and logo color scheme
Font headers that work well with the logo font
Nice to have
• Marine / Maritime theme
relevance to Gulf Coast Region
Should not have
• Dark colors

```html
<!DOCTYPE html>
<html lang="en">
<head>
<meta charset="utf-8">
<title>Corvanta Energy Presentation Slides</title>
<link rel="stylesheet" href="https://fonts.googleapis.com/css2?family=Montserrat:wght@500;800&family=Roboto:wght@400;700&display=swap">
<style>
  :root {
    --page: #eceef0;
    --slide-top: #ffffff;
    --slide-edge: #dcdfe2;
    --ink: #1e1e1e;
    --body: #2b2b2b;
    --green: #5cb646;
    --green-soft: #8fd0a8;
    --sky: #1aa3e0;
    --blue: #1d6cc4;
    --navy: #1b4f9c;
    --orange: #f7a11a;
    --teal: #3aa69a;
    --panel: #e4e6e8;
    --brand: #1d6cc4;
  }
  * { box-sizing: border-box; margin: 0; padding: 0; }
  html, body { width: 1200px; height: 1049px; overflow: hidden; }
  body { background: var(--page); font-family: "Roboto", Arial, sans-serif; color: var(--body); position: relative; }

  .slide {
    position: absolute; width: 558px; height: 314px; overflow: hidden;
    background: radial-gradient(ellipse at 55% 35%, var(--slide-top) 0%, #f4f5f6 55%, var(--slide-edge) 100%);
    box-shadow: 0 3px 10px rgba(0,0,0,.18);
  }
  .col-left { left: 33px; } .col-right { left: 609px; width: 559px; }
  .row-1 { top: 34px; } .row-2 { top: 366px; } .row-3 { top: 705px; }

  .wave { position: absolute; left: 0; bottom: 0; width: 100%; height: 42px; }

  .section-name { position: absolute; font-family: "Montserrat", Arial, sans-serif; font-weight: 500; font-size: 9px; color: var(--green); letter-spacing: .4px; text-transform: uppercase; }
  .slide-title { position: absolute; font-family: "Montserrat", Arial, sans-serif; font-weight: 800; font-size: 15px; color: var(--ink); text-transform: uppercase; letter-spacing: .2px; white-space: nowrap; }
  .slide-title::after { content: ""; position: absolute; left: 0; bottom: -3px; width: 28px; height: 2px; background: var(--ink); }

  .brand { position: absolute; display: flex; flex-direction: column; align-items: center; width: 80px; }
  .brand-dot { width: 24px; height: 24px; border-radius: 50%; background: var(--green); margin-bottom: 3px; }
  .brand-name { font-family: "Montserrat", Arial, sans-serif; font-weight: 800; font-size: 8px; color: var(--brand); text-transform: uppercase; text-align: center; line-height: 1.1; }

  /* pie slide */
  .pie-panel { position: absolute; left: 34px; top: 86px; width: 256px; height: 177px; background: var(--panel); border-radius: 6px; }
  .pie { position: absolute; left: 40px; top: 92px; width: 166px; height: 166px; }
  .pie-legend { position: absolute; left: 224px; top: 148px; list-style: none; font-size: 9px; color: #333; }
  .pie-legend li { display: flex; align-items: center; margin-bottom: 4px; }
  .pie-legend i { width: 7px; height: 7px; margin-right: 5px; display: inline-block; }
  .stat { position: absolute; left: 318px; display: flex; align-items: center; width: 220px; }
  .stat-badge { flex: none; width: 28px; height: 28px; border-radius: 50%; color: #fff; font-family: "Montserrat", Arial, sans-serif; font-weight: 800; font-size: 9px; display: flex; align-items: center; justify-content: center; border: 2px solid #fff; box-shadow: 0 0 0 1px #d8dadc; margin-right: 11px; }
  .stat p { font-size: 7.6px; line-height: 1.3; color: #333; }

  /* column chart */
  .chart { position: absolute; left: 30px; top: 80px; width: 430px; height: 190px; }
  .chart-legend { position: absolute; left: 473px; top: 136px; list-style: none; font-size: 8px; color: #333; }
  .chart-legend li { display: flex; align-items: center; height: 23px; }
  .chart-legend i { width: 12px; height: 9px; margin-right: 8px; display: inline-block; }

  /* points slide */
  .photo-port { position: absolute; left: 0; top: 0; width: 234px; height: 314px; background: linear-gradient(160deg, #f3b34d 0%, #d98a2c 35%, #8a5a2a 70%, #4a3a2e 100%); }
  .points { position: absolute; left: 248px; top: 92px; width: 266px; list-style: none; }
  .points li { position: relative; padding-left: 12px; font-size: 7.4px; line-height: 1.32; color: #333; margin-bottom: 11px; }
  .points li::before { content: ""; position: absolute; left: 0; top: 2px; width: 6px; height: 6px; border-radius: 50%; background: var(--teal); }
  .points b { color: var(--ink); }

  /* text slide */
  .faint-circle { position: absolute; left: 28px; top: 50px; width: 185px; height: 185px; border-radius: 50%; background: #d9e6e6; opacity: .55; }
  .body-copy { position: absolute; font-size: 6.1px; line-height: 1.38; color: #3a3a3a; text-align: justify; }

  /* mission slide */
  .photo-ring { position: absolute; left: 291px; top: 56px; width: 200px; height: 200px; border-radius: 50%; border: 8px solid #5fb3a8; background: radial-gradient(circle at 45% 45%, #f2f3f5 0%, #c6ccd4 45%, #8c96a3 80%, #5d6773 100%); }
  .target { position: absolute; left: 276px; top: 58px; width: 46px; height: 46px; }

  /* features slide */
  .feature { position: absolute; top: 97px; width: 112px; text-align: center; }
  .feature-icon { width: 62px; height: 62px; margin: 0 auto 12px; display: flex; align-items: center; justify-content: center; }
  .feature h3 { font-family: "Roboto", Arial, sans-serif; font-weight: 700; font-size: 10.5px; color: var(--ink); margin-bottom: 3px; }
  .feature p { font-size: 9.5px; line-height: 1.22; color: #333; text-align: left; }
</style>
</head>
<body>

<!-- Slide 1: pie chart -->
<section class="slide col-left row-1">
  <span class="section-name" style="left:28px;top:34px;">Section name here</span>
  <h2 class="slide-title" style="left:28px;top:46px;">Pie chart goes text here</h2>
  <div class="brand" style="right:18px;top:18px;"><span class="brand-dot"></span><span class="brand-name">Corvanta Energy</span></div>
  <div class="pie-panel"></div>
  <svg class="pie" viewBox="-83 -83 166 166" role="img" aria-label="Pie chart: 1st quarter 15%, 2nd quarter 30%, 3rd quarter 5%, 4th quarter 48%">
    <circle r="81" fill="#ffffff" stroke="#3aa69a" stroke-width="3"/>
    <path d="M0 0 L0 -74 A74 74 0 0 1 60.7 -42.3 Z" fill="#1aa3e0" stroke="#fff" stroke-width="1"/>
    <path d="M0 0 L60.7 -42.3 A74 74 0 0 1 18.8 71.6 Z" fill="#1d6cc4" stroke="#fff" stroke-width="1"/>
    <path d="M0 0 L18.8 71.6 A74 74 0 0 1 -4.8 73.8 Z" fill="#f7a11a" stroke="#fff" stroke-width="1"/>
    <path d="M0 0 L-4.8 73.8 A74 74 0 0 1 0 -74 Z" fill="#5cb646" stroke="#fff" stroke-width="1"/>
    <g font-family="Montserrat, Arial, sans-serif" font-weight="800" font-size="14" fill="#fff" text-anchor="middle">
      <text x="30" y="-32">15%</text>
      <text x="42" y="20">30%</text>
      <text x="3" y="58" font-size="12">5%</text>
      <text x="-40" y="5">48%</text>
    </g>
  </svg>
  <ul class="pie-legend">
    <li><i style="background:var(--sky)"></i>1st Qtr</li>
    <li><i style="background:var(--blue)"></i>2nd Qtr</li>
    <li><i style="background:var(--orange)"></i>3rd Qtr</li>
    <li><i style="background:var(--green)"></i>4th Qtr</li>
  </ul>
  <div class="stat" style="top:97px;"><span class="stat-badge" style="background:var(--sky)">15%</span><p>Lorem ipsum dolor sit amet, consectetur adipiscing elit, sed do eiusmod tempor incididunt ut labore et dolore magna aliqua.</p></div>
  <div class="stat" style="top:139px;"><span class="stat-badge" style="background:var(--blue)">30%</span><p>Lorem ipsum dolor sit amet, consectetur adipiscing elit, sed do eiusmod tempor incididunt ut labore et dolore magna aliqua.</p></div>
  <div class="stat" style="top:177px;"><span class="stat-badge" style="background:var(--orange)">5%</span><p>Lorem ipsum dolor sit amet, consectetur adipiscing elit, sed do eiusmod tempor incididunt ut labore et dolore magna aliqua.</p></div>
  <div class="stat" style="top:215px;"><span class="stat-badge" style="background:var(--green)">48%</span><p>Lorem ipsum dolor sit amet, consectetur adipiscing elit, sed do eiusmod tempor incididunt ut labore et dolore magna aliqua.</p></div>
  <svg class="wave" viewBox="0 0 560 42" preserveAspectRatio="none" aria-hidden="true">
    <path d="M0 18 C150 2 320 4 560 16 L560 42 L0 42Z" fill="#bfe3dc"/>
    <path d="M0 26 C160 12 330 12 560 22 L560 42 L0 42Z" fill="#7cc59a"/>
    <path d="M0 30 C180 20 360 22 560 27 L560 42 L0 42Z" fill="#2a8fd4"/>
    <path d="M0 36 C200 31 380 32 560 33 L560 42 L0 42Z" fill="#1b4f9c"/>
  </svg>
</section>

<!-- Slide 2: column chart -->
<section class="slide col-right row-1">
  <span class="section-name" style="left:38px;top:34px;">Section name here</span>
  <h2 class="slide-title" style="left:38px;top:46px;">Coloumn chart goes here</h2>
  <div class="brand" style="right:18px;top:18px;"><span class="brand-dot"></span><span class="brand-name">Corvanta Energy</span></div>
  <svg class="chart" viewBox="0 0 430 190" role="img" aria-label="Column chart of three series across six categories">
    <g stroke="#d4d6d8" stroke-width=".7">
      <line x1="25" y1="5" x2="421" y2="5"/><line x1="25" y1="21.1" x2="421" y2="21.1"/><line x1="25" y1="37.2" x2="421" y2="37.2"/>
      <line x1="25" y1="53.3" x2="421" y2="53.3"/><line x1="25" y1="69.4" x2="421" y2="69.4"/><line x1="25" y1="85.5" x2="421" y2="85.5"/>
      <line x1="25" y1="101.6" x2="421" y2="101.6"/><line x1="25" y1="117.7" x2="421" y2="117.7"/><line x1="25" y1="133.8" x2="421" y2="133.8"/>
      <line x1="25" y1="149.9" x2="421" y2="149.9"/>
    </g>
    <line x1="25" y1="166" x2="421" y2="166" stroke="#888" stroke-width=".8"/>
    <g font-size="7" fill="#444" text-anchor="end" font-family="Roboto, Arial, sans-serif">
      <text x="20" y="8">50</text><text x="20" y="24">45</text><text x="20" y="40">40</text><text x="20" y="56">35</text><text x="20" y="72">30</text>
      <text x="20" y="88">25</text><text x="20" y="104">20</text><text x="20" y="120">15</text><text x="20" y="136">10</text><text x="20" y="152">5</text><text x="20" y="168">0</text>
    </g>
    <!-- bar scale: 3.22 units per value -->
    <g fill="#5cb646">
      <rect x="31" y="27.5" width="13" height="138.5"/><rect x="97" y="82.3" width="13" height="83.7"/><rect x="163" y="53.3" width="13" height="112.7"/>
      <rect x="229" y="69.4" width="13" height="96.6"/><rect x="295" y="21.1" width="13" height="144.9"/><rect x="361" y="66.2" width="13" height="99.8"/>
    </g>
    <g fill="#1d7ccc">
      <rect x="45" y="88.7" width="13" height="77.3"/><rect x="111" y="24.3" width="13" height="141.7"/><rect x="177" y="108" width="13" height="58"/>
      <rect x="243" y="85.5" width="13" height="80.5"/><rect x="309" y="56.5" width="13" height="109.5"/><rect x="375" y="56.5" width="13" height="109.5"/>
    </g>
    <g fill="#22c1ea">
      <rect x="59" y="101.6" width="13" height="64.4"/><rect x="125" y="101.6" width="13" height="64.4"/><rect x="191" y="69.4" width="13" height="96.6"/>
      <rect x="257" y="37.2" width="13" height="128.8"/><rect x="323" y="72.6" width="13" height="93.4"/><rect x="389" y="34" width="13" height="132"/>
    </g>
    <g font-size="9" fill="#222" text-anchor="middle" font-family="Roboto, Arial, sans-serif">
      <text x="51" y="180">Category 1</text><text x="117" y="180">Category 2</text><text x="183" y="180">Category 3</text>
      <text x="249" y="180">Category 4</text><text x="315" y="180">Category 4</text><text x="381" y="180">Category 5</text>
    </g>
  </svg>
  <ul class="chart-legend">
    <li><i style="background:#5cb646"></i>Series 1</li>
    <li><i style="background:#1d7ccc"></i>Series 2</li>
    <li><i style="background:#22c1ea"></i>Series 3</li>
  </ul>
  <svg class="wave" viewBox="0 0 560 42" preserveAspectRatio="none" aria-hidden="true">
    <path d="M0 18 C150 2 320 4 560 16 L560 42 L0 42Z" fill="#bfe3dc"/>
    <path d="M0 26 C160 12 330 12 560 22 L560 42 L0 42Z" fill="#7cc59a"/>
    <path d="M0 30 C180 20 360 22 560 27 L560 42 L0 42Z" fill="#2a8fd4"/>
    <path d="M0 36 C200 31 380 32 560 33 L560 42 L0 42Z" fill="#1b4f9c"/>
  </svg>
</section>

<!-- Slide 3: many points -->
<section class="slide col-left row-2">
  <div class="photo-port" role="img" aria-label="Photo of port gantry cranes lifting a shipping container at sunset"></div>
  <span class="section-name" style="left:248px;top:40px;">Section name here</span>
  <h2 class="slide-title" style="left:248px;top:52px;">Many points goes here</h2>
  <div class="brand" style="right:18px;top:18px;"><span class="brand-dot"></span><span class="brand-name">Corvanta Energy</span></div>
  <ul class="points">
    <li><b>Lorem Ipsum</b> is simply dummy text of the printing and typesetting industry. Lorem Ipsum has been the industry's standard dummy text ever since.</li>
    <li><b>Lorem Ipsum</b> is simply dummy text of the printing and typesetting industry. Lorem Ipsum has been the industry's standard dummy text ever since.</li>
    <li><b>Lorem Ipsum</b> is simply dummy text of the printing and typesetting industry. Lorem Ipsum has been the industry's standard dummy text ever since.</li>
    <li><b>Lorem Ipsum</b> is simply dummy text of the printing and typesetting industry. Lorem Ipsum has been the industry's standard dummy text ever since.</li>
    <li><b>Lorem Ipsum</b> is simply dummy text of the printing and typesetting industry. Lorem Ipsum has been the industry's standard dummy text ever since.</li>
  </ul>
  <svg class="wave" viewBox="0 0 560 42" preserveAspectRatio="none" aria-hidden="true">
    <path d="M0 18 C150 2 320 4 560 16 L560 42 L0 42Z" fill="#bfe3dc"/>
    <path d="M0 26 C160 12 330 12 560 22 L560 42 L0 42Z" fill="#7cc59a"/>
    <path d="M0 30 C180 20 360 22 560 27 L560 42 L0 42Z" fill="#2a8fd4"/>
    <path d="M0 36 C200 31 380 32 560 33 L560 42 L0 42Z" fill="#1b4f9c"/>
  </svg>
</section>

<!-- Slide 4: text slide -->
<section class="slide col-right row-2">
  <div class="faint-circle" aria-hidden="true"></div>
  <div class="brand" style="right:18px;top:24px;"><span class="brand-dot"></span><span class="brand-name">Corvanta Energy</span></div>
  <span class="section-name" style="left:252px;top:89px;">Section name here</span>
  <h2 class="slide-title" style="left:252px;top:101px;">Text slide goes here</h2>
  <p class="body-copy" style="left:252px;top:124px;width:282px;">Lorem ipsum dolor sit amet, consectetur adipiscing elit, sed do eiusmod tempor incididunt ut labore et dolore magna aliqua. Ut enim ad minim veniam, quis nostrud exercitation ullamco laboris nisi ut aliquip ex ea commodo consequat. Duis aute irure dolor in reprehenderit in voluptate velit esse cillum dolore eu fugiat nulla pariatur. Excepteur sint occaecat cupidatat non proident, sunt in culpa qui officia deserunt mollit anim id est laborum. Lorem ipsum dolor sit amet, consectetur adipiscing elit, sed do eiusmod tempor incididunt ut labore et dolore magna aliqua. Ut enim ad minim veniam, quis nostrud exercitation ullamco laboris nisi ut aliquip ex ea commodo consequat. Duis aute irure dolor in reprehenderit in voluptate velit esse cillum dolore eu fugiat nulla pariatur. Excepteur sint occaecat cupidatat non proident, sunt in culpa qui officia deserunt mollit anim id est laborum.</p>
  <svg class="wave" viewBox="0 0 560 42" preserveAspectRatio="none" aria-hidden="true">
    <path d="M0 18 C150 2 320 4 560 16 L560 42 L0 42Z" fill="#bfe3dc"/>
    <path d="M0 26 C160 12 330 12 560 22 L560 42 L0 42Z" fill="#7cc59a"/>
    <path d="M0 30 C180 20 360 22 560 27 L560 42 L0 42Z" fill="#2a8fd4"/>
    <path d="M0 36 C200 31 380 32 560 33 L560 42 L0 42Z" fill="#1b4f9c"/>
  </svg>
</section>

<!-- Slide 5: mission -->
<section class="slide col-left row-3">
  <div class="brand" style="left:26px;top:20px;"><span class="brand-dot"></span><span class="brand-name">Corvanta Energy</span></div>
  <span class="section-name" style="left:28px;top:87px;color:var(--sky);">Section name here</span>
  <h2 class="slide-title" style="left:28px;top:99px;">Our mission</h2>
  <p class="body-copy" style="left:28px;top:128px;width:200px;">Lorem ipsum dolor sit amet, consectetur adipiscing elit, sed do eiusmod tempor incididunt ut labore et dolore magna aliqua. Ut enim ad minim veniam, quis nostrud exercitation ullamco laboris nisi ut aliquip ex ea commodo consequat.</p>
  <p class="body-copy" style="left:28px;top:190px;width:200px;">Lorem ipsum dolor sit amet, consectetur adipiscing elit, sed do eiusmod tempor incididunt ut labore et dolore magna aliqua. Ut enim ad minim veniam, quis nostrud exercitation ullamco laboris nisi ut aliquip ex ea commodo consequat.</p>
  <div class="photo-ring" role="img" aria-label="Photo of a team stacking hands together in the centre"></div>
  <svg class="target" viewBox="0 0 46 46" aria-hidden="true">
    <circle cx="23" cy="23" r="21" fill="#fff" stroke="#3aa69a" stroke-width="2"/>
    <circle cx="23" cy="23" r="14" fill="none" stroke="#3aa69a" stroke-width="3"/>
    <circle cx="23" cy="23" r="7" fill="none" stroke="#3aa69a" stroke-width="3"/>
    <circle cx="23" cy="23" r="2.5" fill="#3aa69a"/>
    <path d="M23 23 L38 8" stroke="#3aa69a" stroke-width="2"/>
    <path d="M34 6 L40 6 L40 12" fill="none" stroke="#3aa69a" stroke-width="2"/>
  </svg>
  <svg class="wave" viewBox="0 0 560 42" preserveAspectRatio="none" aria-hidden="true">
    <path d="M0 18 C150 2 320 4 560 16 L560 42 L0 42Z" fill="#bfe3dc"/>
    <path d="M0 26 C160 12 330 12 560 22 L560 42 L0 42Z" fill="#7cc59a"/>
    <path d="M0 30 C180 20 360 22 560 27 L560 42 L0 42Z" fill="#2a8fd4"/>
    <path d="M0 36 C200 31 380 32 560 33 L560 42 L0 42Z" fill="#1b4f9c"/>
  </svg>
</section>

<!-- Slide 6: four features -->
<section class="slide col-right row-3">
  <span class="section-name" style="left:38px;top:38px;">Section name here</span>
  <h2 class="slide-title" style="left:38px;top:50px;">Your heading goes here</h2>
  <div class="brand" style="right:18px;top:18px;"><span class="brand-dot"></span><span class="brand-name">Corvanta Energy</span></div>

  <div class="feature" style="left:30px;">
    <div class="feature-icon" style="background:var(--sky)">
      <svg width="36" height="36" viewBox="0 0 36 36" aria-hidden="true"><circle cx="18" cy="15" r="8" fill="none" stroke="#fff" stroke-width="2.2"/><rect x="14" y="24" width="8" height="3" fill="#fff"/><rect x="15" y="28.5" width="6" height="2.5" fill="#fff"/><path d="M18 2v3M6 6l2 2M30 6l-2 2M3 15h3M30 15h3" stroke="#fff" stroke-width="2"/></svg>
    </div>
    <h3>Lorem Ipsum dollar</h3>
    <p>Lorem ipsum dolor sit amet, consectetur adipiscing elit. Ut enim ad minim veniam, quis nostrud exercitation ullamco laboris nisi ut aliquip ex ea commodo consequat.</p>
  </div>
  <div class="feature" style="left:159px;">
    <div class="feature-icon" style="background:var(--green)">
      <svg width="36" height="36" viewBox="0 0 36 36" aria-hidden="true"><rect x="8" y="4" width="20" height="26" fill="none" stroke="#fff" stroke-width="2"/><path d="M12 10h12M12 14h12M12 18h8" stroke="#fff" stroke-width="1.8"/><path d="M6 30l6-5 6 4 6-4 6 5" fill="none" stroke="#fff" stroke-width="2"/></svg>
    </div>
    <h3>Lorem Ipsum dollar</h3>
    <p>Lorem ipsum dolor sit amet, consectetur adipiscing elit. Ut enim ad minim veniam, quis nostrud exercitation ullamco laboris nisi ut aliquip ex ea commodo consequat.</p>
  </div>
  <div class="feature" style="left:287px;">
    <div class="feature-icon" style="background:var(--orange)">
      <svg width="36" height="36" viewBox="0 0 36 36" aria-hidden="true"><rect x="4" y="5" width="20" height="18" rx="2" fill="none" stroke="#fff" stroke-width="2"/><text x="14" y="19" font-family="Roboto, Arial, sans-serif" font-weight="700" font-size="13" fill="#fff" text-anchor="middle">$</text><path d="M20 33v-9a2 2 0 0 1 4 0v4l6 1v4" fill="none" stroke="#fff" stroke-width="2"/></svg>
    </div>
    <h3>Lorem Ipsum dollar</h3>
    <p>Lorem ipsum dolor sit amet, consectetur adipiscing elit. Ut enim ad minim veniam, quis nostrud exercitation ullamco laboris nisi ut aliquip ex ea commodo consequat.</p>
  </div>
  <div class="feature" style="left:415px;">
    <div class="feature-icon" style="background:var(--navy)">
      <svg width="36" height="36" viewBox="0 0 36 36" aria-hidden="true"><rect x="6" y="16" width="5" height="14" fill="#fff"/><rect x="13" y="8" width="5" height="22" fill="#fff"/><rect x="20" y="12" width="5" height="18" fill="#fff"/><circle cx="22" cy="20" r="6" fill="#1b4f9c" stroke="#fff" stroke-width="2"/><path d="M26 24l5 5" stroke="#fff" stroke-width="3"/></svg>
    </div>
    <h3>Lorem Ipsum dollar</h3>
    <p>Lorem ipsum dolor sit amet, consectetur adipiscing elit. Ut enim ad minim veniam, quis nostrud exercitation ullamco laboris nisi ut aliquip ex ea commodo consequat.</p>
  </div>
  <svg class="wave" viewBox="0 0 560 42" preserveAspectRatio="none" aria-hidden="true">
    <path d="M0 18 C150 2 320 4 560 16 L560 42 L0 42Z" fill="#bfe3dc"/>
    <path d="M0 26 C160 12 330 12 560 22 L560 42 L0 42Z" fill="#7cc59a"/>
    <path d="M0 30 C180 20 360 22 560 27 L560 42 L0 42Z" fill="#2a8fd4"/>
    <path d="M0 36 C200 31 380 32 560 33 L560 42 L0 42Z" fill="#1b4f9c"/>
  </svg>
</section>

</body>
</html>
```